Keystone Haulers Billboard design

I need two billboard designs using our logo and adding a few words Looking for a black background with our logo and wording in either purple or white.

need it to have our website keystonehaulers-example.com. phone number 555 201 4387

Also have 16/20/30 yard dumpsters available!

one billboard is size 7x21 feet the other is 15x 21 ft

Target Market(s)

Contractors, home owners

Requirements
Must have
• Use font similar to logo that is eye catching

```html
<!DOCTYPE html>
<html lang="en">
<head>
<meta charset="utf-8">
<title>Keystone Haulers Billboard</title>
<link href="https://fonts.googleapis.com/css2?family=Bebas+Neue&family=Montserrat:wght@400;700&family=Poppins:wght@700&display=swap" rel="stylesheet">
<style>
  :root {
    --black: #000000;
    --purple: #7b3f9e;
    --white: #ffffff;
    --stage: #e9e9ec;
    --truck-light: #d9dadd;
    --truck-dark: #3a3a3e;
  }
  html, body {
    margin: 0;
    padding: 0;
    width: 1200px;
    height: 1175px;
    overflow: hidden;
    background: var(--stage);
  }
  .billboard {
    position: absolute;
    left: 0;
    top: 374px;
    width: 1200px;
    height: 427px;
    background: var(--black);
    overflow: hidden;
    font-family: "Bebas Neue", "Oswald", sans-serif;
    color: var(--white);
  }
  .sizes {
    position: absolute;
    left: 40px;
    top: 36px;
    margin: 0;
    font-size: 94px;
    line-height: 1;
    font-weight: 400;
    letter-spacing: 1px;
  }
  .dumpsters-tag {
    position: absolute;
    left: 20px;
    top: 125px;
    width: 341px;
    height: 97px;
    background: var(--purple);
    border-radius: 7px;
    font-size: 90px;
    line-height: 97px;
    text-align: center;
    letter-spacing: 1px;
  }
  .available {
    position: absolute;
    left: 378px;
    top: 125px;
    font-size: 90px;
    line-height: 97px;
    letter-spacing: 1px;
  }
  .web-band {
    position: absolute;
    left: 0;
    top: 281px;
    width: 506px;
    height: 52px;
  }
  .web-text {
    position: absolute;
    left: 76px;
    top: 281px;
    height: 52px;
    line-height: 52px;
    font-family: "Montserrat", sans-serif;
    font-size: 27px;
    font-weight: 400;
    color: var(--white);
  }
  .web-text strong { font-weight: 700; }
  .laptop-icon {
    position: absolute;
    left: 24px;
    top: 291px;
    width: 38px;
    height: 32px;
  }
  .phone-box {
    position: absolute;
    left: 0;
    top: 336px;
    width: 96px;
    height: 91px;
    background: var(--black);
  }
  .phone-icon {
    position: absolute;
    left: 18px;
    top: 346px;
    width: 60px;
    height: 64px;
  }
  .phone-strip {
    position: absolute;
    left: 96px;
    top: 336px;
    width: 598px;
    height: 91px;
    background: var(--white);
  }
  .phone-number {
    position: absolute;
    left: 112px;
    top: 336px;
    height: 91px;
    line-height: 95px;
    font-family: "Poppins", sans-serif;
    font-weight: 700;
    font-size: 84px;
    color: var(--black);
    letter-spacing: 1px;
  }
  .truck-band {
    position: absolute;
    left: 753px;
    top: 295px;
    width: 447px;
    height: 132px;
    background: var(--purple);
  }
  .brand-name {
    position: absolute;
    left: 744px;
    top: 22px;
    width: 430px;
    text-align: center;
    color: var(--white);
    font-size: 92px;
    line-height: 0.9;
    letter-spacing: 2px;
  }
  .brand-name span {
    display: block;
    font-size: 58px;
    letter-spacing: 6px;
  }
  .truck-photo {
    position: absolute;
    left: 694px;
    top: 180px;
    width: 480px;
    height: 245px;
    border-radius: 10px;
    background: linear-gradient(160deg, var(--truck-light) 0%, #f4f4f5 45%, var(--truck-dark) 100%);
  }
</style>
</head>
<body>
  <section class="billboard">
    <h1 class="sizes">16/20/30 YARD</h1>
    <div class="dumpsters-tag">DUMPSTERS</div>
    <div class="available">AVAILABLE!</div>

    <svg class="web-band" viewBox="0 0 506 52" aria-hidden="true">
      <polygon points="0,0 491,0 506,52 0,52" fill="var(--purple)"/>
    </svg>
    <svg class="laptop-icon" viewBox="0 0 38 32" aria-hidden="true">
      <rect x="6" y="3" width="26" height="19" rx="2" fill="none" stroke="var(--white)" stroke-width="3"/>
      <rect x="1" y="25" width="36" height="4" rx="1.5" fill="var(--white)"/>
    </svg>
    <div class="web-text">keystone<strong>haulers</strong>-example.com</div>

    <div class="phone-box"></div>
    <svg class="phone-icon" viewBox="0 0 60 64" aria-hidden="true">
      <path d="M12 6 L22 4 L28 20 L21 25 Q26 38 37 45 L43 39 L57 47 L54 58 Q48 62 40 59 Q14 46 6 20 Q5 11 12 6 Z" fill="var(--white)"/>
      <path d="M36 14 Q44 16 46 24" fill="none" stroke="var(--white)" stroke-width="4" stroke-linecap="round"/>
      <path d="M38 4 Q53 7 56 22" fill="none" stroke="var(--white)" stroke-width="4" stroke-linecap="round"/>
    </svg>
    <div class="phone-strip"></div>
    <div class="phone-number">555 201 4387</div>

    <div class="truck-band"></div>
    <div class="brand-name">KEYSTONE<span>HAULERS</span></div>
    <div class="truck-photo" role="img" aria-label="Photo of a white roll-off dumpster truck with black hoist arms"></div>
  </section>
</body>
</html>
```